Alder Court Parking Lot Flyer

I need a 1/2 page flyer to look and feel like my website. With all the relevant information like phone # and map to our office. It needs to look and feel like a shortened or brief version of our website but on paper. I would like the colors to be the same palette as the website and I would like the flyer to be full color front and back. The web address is pinonridgelegalteam.com
Our logo is on the website and all relevant information can be viewed there as well. Please include our web address on the flyer as well.
This is for a Law Firm so it needs to be very PROFESSIONAL Looking.
DO NOT USE OUR PHOTOGRAPHS OR PICTURES OF US.

Target Market(s)

People visiting the courthouse who need to hire a criminal defense attorney immediately.

Industry/Entity Type

Court

Font styles to use
Serif

Colors

Designer to choose colors to be used in the design.

Requirements
Must have
• Contact information and map. Web address is crucial as well.

```html
<!DOCTYPE html>
<html lang="en">
<head>
<meta charset="utf-8">
<title>Pinon Ridge Legal Team – Alder Court Flyer</title>
<link href="https://fonts.googleapis.com/css2?family=Cinzel:wght@400;600&family=Playfair+Display:wght@700&family=Roboto+Slab:wght@400;700&family=Open+Sans:wght@400;700;800&display=swap" rel="stylesheet">
<style>
  :root{
    --bg:#e7e4dc;
    --charcoal:#262523;
    --charcoal-2:#34322e;
    --tan:#b9b08d;
    --tan-light:#cec7a6;
    --tan-dark:#8f8768;
    --cream:#efe9d6;
    --ink:#1d1c1a;
    --white:#ffffff;
  }
  *{box-sizing:border-box;margin:0;padding:0}
  html,body{width:1200px;height:1000px;overflow:hidden}
  body{background:var(--bg);position:relative;font-family:"Open Sans",sans-serif;color:var(--ink)}

  .flyer{position:absolute;left:250px;width:700px;height:453px;overflow:hidden;box-shadow:0 6px 18px rgba(0,0,0,.25)}
  .flyer--front{top:30px;background:var(--charcoal)}
  .flyer--back{top:513px;background:var(--tan)}

  /* front */
  .front-photo{position:absolute;inset:0 0 110px 0;
    background:linear-gradient(120deg,#4a4a46 0%,#6d6a63 35%,#a59d8c 60%,#d8d0bd 80%,#8a8272 100%)}
  .front-band{position:absolute;left:0;right:0;bottom:0;height:110px;
    background:linear-gradient(90deg,#3b3a37,#1c1b1a);display:flex;align-items:center;padding-left:40px;gap:22px}
  .mark-circle{width:52px;height:52px;border:2px solid var(--cream);border-radius:50%;flex:none}
  .firm-name{font-family:"Cinzel",serif;font-weight:400;color:var(--cream);font-size:33px;letter-spacing:2px}
  .tagline{position:absolute;right:40px;top:60px;text-align:left;color:var(--white)}
  .tagline h1{font-family:"Playfair Display",serif;font-size:36px;line-height:1.15}
  .attorneys{margin-top:14px;font-family:"Open Sans",sans-serif;font-weight:800;font-size:12px;letter-spacing:.5px;line-height:1.6}

  /* back */
  .services{position:absolute;left:0;top:0;width:420px;height:343px;
    background:linear-gradient(160deg,var(--tan-light),var(--tan));padding:26px 18px 0 24px;display:flex;gap:16px}
  .service-list{list-style:none;font-family:"Roboto Slab",serif;font-weight:700;font-size:14.5px;line-height:1.12;color:var(--ink)}
  .service-list li{position:relative;padding-left:18px;margin-bottom:7px;text-transform:uppercase}
  .service-list li::before{content:"";position:absolute;left:2px;top:3px;width:5px;height:5px;
    border-right:2px solid var(--ink);border-bottom:2px solid var(--ink);transform:rotate(45deg)}
  .col-1{width:185px}
  .col-2{width:190px}
  .about{font-size:9.5px;line-height:1.45;margin:8px 0 10px}
  .call{font-size:10.5px;font-weight:800;line-height:1.4}

  .side{position:absolute;left:420px;top:0;width:280px;height:343px;background:var(--charcoal)}
  .side-header{height:40px;display:flex;align-items:center;gap:10px;padding-left:14px}
  .side-header .mark-circle{width:24px;height:24px;border-width:1.5px}
  .side-header .firm-name{font-size:14px;letter-spacing:1px}
  .info-box{background:var(--white);margin:0 10px;padding:9px 11px;height:132px;font-size:7.6px;line-height:1.4}
  .info-box h2{font-family:"Roboto Slab",serif;font-weight:700;font-size:9px;text-transform:uppercase;margin-bottom:3px}
  .info-box p{margin-bottom:6px}
  .photo-strip{margin:8px 10px 0;height:92px;background:linear-gradient(90deg,#9a9384,#d7d1c4 50%,#7b756a)}
  .phone{font-family:"Open Sans",sans-serif;font-weight:800;color:var(--white);font-size:34px;padding:6px 14px 0;letter-spacing:.5px}
  .web{color:var(--white);font-weight:700;font-size:12px;padding-left:14px}

  .locate{position:absolute;left:0;bottom:0;width:700px;height:110px;background:var(--charcoal-2);display:flex;align-items:center;gap:26px;padding-left:22px;border-top:3px solid var(--tan-dark)}
  .map{width:190px;height:86px;background:linear-gradient(135deg,#1f1e1c,#3d3b36)}
  .arrest h3{font-family:"Roboto Slab",serif;font-weight:700;color:var(--cream);font-size:15px;line-height:1.3}
  .address{margin-top:8px;color:var(--cream);font-size:12px;line-height:1.4}
</style>
</head>
<body>

<section class="flyer flyer--front">
  <div class="front-photo" role="img" aria-label="Sepia photograph of a man in a grey suit standing before a bright window"></div>
  <div class="tagline">
    <h1>Clearing your name<br>is our #1 priority</h1>
    <p class="attorneys">DANIEL ASHFORD<br>MARCUS ELLERY</p>
  </div>
  <div class="front-band">
    <span class="mark-circle"></span>
    <span class="firm-name">PINON RIDGE LEGAL TEAM</span>
  </div>
</section>

<section class="flyer flyer--back">
  <div class="services">
    <ul class="service-list col-1">
      <li>DUI/DWI Defense</li>
      <li>Domestic Violence</li>
      <li>Drug Crimes</li>
      <li>Assault &amp; Battery</li>
      <li>Homicide,<br>Attempted Murder</li>
      <li>Larceny</li>
      <li>Minor in Possession</li>
      <li>Probation<br>Violations</li>
      <li>Resisting Arrest,<br>Public Affray</li>
    </ul>
    <div class="col-2">
      <ul class="service-list">
        <li>Robbery, Burglary,<br>and Theft</li>
        <li>Sex Crimes</li>
        <li>White Collar Crimes</li>
      </ul>
      <p class="about">Since 1997, the <strong>Pinon Ridge Legal Team</strong> in Alder Springs has focused on protecting the rights of our clients. We employ bold strategies and aggressive representation to achieve these goals. Our firm consists of two attorneys who are committed to success for our clients, and a dedicated staff working diligently to achieve these goals.</p>
      <p class="call">Call us at 555-200-4817 or contact us using our form today.</p>
    </div>
  </div>

  <div class="side">
    <div class="side-header">
      <span class="mark-circle"></span>
      <span class="firm-name">PINON RIDGE LEGAL TEAM</span>
    </div>
    <div class="info-box">
      <h2>We offer a free initial consultation</h2>
      <p>Our experienced trial lawyers meet with every new client at no cost to review the charges, explain the process and outline the strongest path toward a fair result.</p>
      <h2>Personalized legal representation<br>our strategy for success</h2>
      <p>Each case is built around the client. We study the evidence, challenge every weak point and keep you informed from the first hearing to the final verdict.</p>
    </div>
    <div class="photo-strip" role="img" aria-label="Collage of photographs showing attorneys meeting clients in an office"></div>
    <p class="phone">555.200.481</p>
    <p class="web">www.pinonridgelegalteam.com</p>
  </div>

  <div class="locate">
    <div class="map" role="img" aria-label="Street map showing the office location near Alder Court"></div>
    <div class="arrest">
      <h3>If you have been arrested for any<br>criminal offense, do not hesitate<br>to contact our law offices.</h3>
      <p class="address">415 Juniper Street NW, Alder Springs,<br>NM 87000</p>
    </div>
  </div>
</section>

</body>
</html>
```